Vape Brand Cartoon Packaging Design

I AM NOT PICKY!! Just need to get the basic job done and I will be happy. To start we need a text logo for our brand "Nelu Glaze" vape cartridges that is colorful, with a cartoonish design. We have 3 flavors we are starting with that need there own custom logo: Velvet Parfait (colorful pink packaging with ice cream sherbert incorporated in the cartoon design), Picnic Torte (blue background with a white cake cartoon design), and Harbor Biscuits (orange packaging with cartoon animated zimbo cookies acting crazy/fighting on it). I dont care if the images are sourced from google images or wherever. See the uploaded files for guidance I want them extremely similar to that packaging. The packaging is roughly 1.5 inches wide and 2.5 inches tall.
Where the packaging says "pine hollow uncommons" I want my brand name "Nelu Glaze", underneath it I want it to say "vape cartridge" just like in the picture. I also want the flavors in the same area on the package and for them all to say HYBRID and 1.0 gram in the same spot. Instead of 1.0 gram though have it say 1000 mg. To reiterate I want the packaging very similar to the packaging in the picture. There will be other flavors added in the near future so ideally I want someone I can work with in the long term!
Nelu Glaze

```html
<!DOCTYPE html>
<html lang="en">
<head>
<meta charset="utf-8">
<title>Nelu Glaze — Vape Cartridge Packaging</title>
<link href="https://fonts.googleapis.com/css2?family=Rye&family=Source+Sans+3:wght@700&family=Roboto+Condensed:wght@700&display=swap" rel="stylesheet">
<style>
  :root {
    --canvas: #fdfcee;
    --ink: #3d1020;
    --pink: #f4a6c9;
    --pink-text: #e0168a;
    --orange: #f6a033;
    --orange-deep: #b8732c;
    --brown: #4a2a12;
    --blue-deep: #3e4fa8;
    --navy: #101640;
    --logo-pink: #e9a7c6;
    --logo-orange: #f0a673;
    --logo-blue: #8fc9ef;
    --white: #ffffff;
  }
  * { box-sizing: border-box; margin: 0; padding: 0; }
  html, body { width: 1200px; height: 1000px; overflow: hidden; background: var(--canvas); }
  .canvas { position: relative; width: 1200px; height: 1000px; }

  .brand-lockup { position: absolute; top: 100px; width: 340px; text-align: center; }
  .brand-name { font-family: "Rye", serif; font-size: 56px; line-height: 66px; }
  .brand-sub {
    font-family: "Source Sans 3", sans-serif; font-weight: 700;
    font-size: 14px; line-height: 18px; letter-spacing: 0.5px; color: var(--ink); margin-top: 42px;
  }
  .lockup-pink { left: 10px; }    .lockup-pink .brand-name { color: var(--logo-pink); }
  .lockup-orange { left: 420px; } .lockup-orange .brand-name { color: var(--logo-orange); }
  .lockup-blue { left: 830px; }   .lockup-blue .brand-name { color: var(--logo-blue); }

  .pack { position: absolute; top: 275px; width: 349px; height: 582px; overflow: hidden; text-align: center; }
  .pack-pink { left: 22px; background: radial-gradient(circle at 50% 60%, #fbd0e2, var(--pink) 75%); }
  .pack-orange { left: 420px; background: radial-gradient(circle at 50% 55%, #fcc46a, var(--orange) 70%); }
  .pack-blue { left: 811px; background: radial-gradient(circle at 50% 50%, #8a97d6, var(--blue-deep) 85%); }

  .top-wash { position: absolute; left: 0; top: 0; width: 100%; height: 120px; }
  .pack-pink .top-wash { background: linear-gradient(rgba(192,80,127,0.85), rgba(192,80,127,0)); }
  .pack-orange .top-wash { background: linear-gradient(rgba(184,115,44,0.8), rgba(184,115,44,0)); }
  .wave-bottom { position: absolute; left: 0; bottom: 0; width: 100%; height: 90px;
    background: linear-gradient(rgba(184,115,44,0), rgba(184,115,44,0.8) 45%); }

  .flavor-name {
    position: absolute; left: 0; top: 18px; width: 100%; z-index: 2;
    font-family: "Rye", serif; font-weight: 400; font-size: 31px; line-height: 40px;
    letter-spacing: 1px; color: var(--white);
    text-shadow: 2px 0 var(--ink), -2px 0 var(--ink), 0 2px var(--ink), 0 -2px var(--ink),
                 1.5px 1.5px var(--ink), -1.5px 1.5px var(--ink), 1.5px -1.5px var(--ink), -1.5px -1.5px var(--ink);
  }
  .pack .brand-name { position: absolute; left: 0; width: 100%; font-size: 50px; line-height: 60px; }
  .pack .brand-sub { position: absolute; left: 0; width: 100%; margin: 0; font-size: 13px; }
  .pack-pink .brand-name { top: 135px; color: #fbe3ee; }
  .pack-pink .brand-sub { top: 218px; }
  .pack-orange .brand-name { top: 120px; color: #fde0c8; }
  .pack-orange .brand-sub { top: 197px; }
  .pack-blue .brand-name { top: 125px; color: #d8efff; }
  .pack-blue .brand-sub { top: 206px; }

  .art { position: absolute; }
  .art-sherbet { left: 75px; top: 262px; width: 200px; height: 240px; border-radius: 50% 50% 20% 20%;
    background: radial-gradient(circle at 50% 40%, #f9d77a, #f7a3b8 55%, #e21a7f 100%); }
  .art-biscuits { left: 85px; top: 225px; width: 200px; height: 245px; border-radius: 40%;
    background: radial-gradient(circle at 50% 40%, #f1d4a2, #e7b87a 50%, #3b2414 100%); }
  .art-torte { left: 55px; top: 235px; width: 245px; height: 262px; border-radius: 10px;
    background: linear-gradient(#fdf4ea, #ffffff 60%, #e4cdb4); }

  .strain { position: absolute; left: 0; width: 100%; top: 520px; z-index: 2;
    font-family: "Roboto Condensed", sans-serif; font-weight: 700; font-size: 20px; line-height: 22px; }
  .dose { font-size: 15px; }
  .pack-pink .strain { color: var(--pink-text); }
  .pack-orange .strain { color: var(--brown); }
  .pack-blue .strain { color: var(--navy); }
</style>
</head>
<body>
<main class="canvas">
  <div class="brand-lockup lockup-pink"><div class="brand-name">Nelu Glaze</div><div class="brand-sub">VAPE CARTRIDGE</div></div>
  <div class="brand-lockup lockup-orange"><div class="brand-name">Nelu Glaze</div><div class="brand-sub">VAPE CARTRIDGE</div></div>
  <div class="brand-lockup lockup-blue"><div class="brand-name">Nelu Glaze</div><div class="brand-sub">VAPE CARTRIDGE</div></div>

  <section class="pack pack-pink">
    <div class="top-wash"></div>
    <h2 class="flavor-name">VELVET<br>PARFAIT</h2>
    <div class="brand-name">Nelu Glaze</div>
    <div class="brand-sub">VAPE CARTRIDGE</div>
    <div class="art art-sherbet" role="img" aria-label="Cartoon stack of sherbet scoops in a pink bowl"></div>
    <div class="strain">HYBRID<br><span class="dose">1000 MG</span></div>
  </section>

  <section class="pack pack-orange">
    <div class="top-wash"></div>
    <div class="wave-bottom"></div>
    <h2 class="flavor-name">HARBOR<br>BISCUITS</h2>
    <div class="brand-name">Nelu Glaze</div>
    <div class="brand-sub">VAPE CARTRIDGE</div>
    <div class="art art-biscuits" role="img" aria-label="Cartoon cocoa mug with lively zimbo cookies scuffling around it"></div>
    <div class="strain">HYBRID<br><span class="dose">1000 MG</span></div>
  </section>

  <section class="pack pack-blue">
    <h2 class="flavor-name">PICNIC<br>TORTE</h2>
    <div class="brand-name">Nelu Glaze</div>
    <div class="brand-sub">VAPE CARTRIDGE</div>
    <div class="art art-torte" role="img" aria-label="Three-tier white cake with draped icing and brown hearts"></div>
    <div class="strain">HYBRID<br><span class="dose">1000 MG</span></div>
  </section>
</main>
</body>
</html>
```